Education, Principal Business Card

I would like a double-sided, full colour business card for my personal use as Principal of a Primary School. The card needs to feature the school logo (.jpeg and .eps files attached), along with the following details:

Miles Torvek
PRINCIPAL
Garrow Primary School
318 Kessel Road HIGH WYCOMBE WA 6057
t: (08) 9362 1504 f: (08) 9362 7190 m: 0413 582 947
e: Miles.Torvek@pupilhub.wa.edu.au
w: www.garrowps.wa.edu.au
l: au.linkfolio.net/in/milestorvek/

The arrangement of details between front and back of the card is at your discretion as are fonts. Colours limited to black, red and white. Looking for bold and modern / clean design LINK a print-ready publication.

Target Market(s)

Parents, colleagues, professionals.

Industry/Entity Type

School

Contact Information for Business Card

As per project brief.

Font styles to use
Serif
Sans Serif
Decorative
Script

Colors
ea1f26
ffffff
000000

Requirements
Must have
• All of the listed contact details. Strong feature of the school logo and corporate colours of black, red and white.
Nice to have
• Rounded corners design a plus. If all details could be placed on the front, a bold education themed quote on the reverse side of the card would be great. Suggested quotes;
• “Education is the most powerful weapon which you can use to change the world.”
• ― Oswin Tembeka
• "Be who you are
• and say what you feel
• because those who mind don't matter
• and those who matter don't mind." Dr Plimb
Should not have
• Clip art, Times New Roman, Arial or boring fonts, low resolution image (please use the vector file if possible).

```html
<!DOCTYPE html>
<html lang="en">
<head>
<meta charset="utf-8">
<title>Garrow Primary School – Principal Business Card</title>
<link rel="stylesheet" href="https://fonts.googleapis.com/css2?family=Anton&family=Oswald:wght@500;700&display=swap">
<style>
  :root {
    --red: #ea1f26;
    --black: #000000;
    --white: #ffffff;
    --grey: #6b6b6b;
    --slate: #3d3636;
    --backdrop: #d9d9d9;
    --mark-tone: #1a1a1a;
  }
  * { box-sizing: border-box; margin: 0; padding: 0; }
  html, body { width: 1200px; height: 900px; overflow: hidden; }
  body {
    background: var(--backdrop);
    font-family: "Oswald", "Arial Narrow", sans-serif;
    color: var(--black);
    display: flex;
    align-items: center;
    justify-content: center;
    gap: 90px;
  }
  .card {
    position: relative;
    width: 380px;
    height: 620px;
    background: var(--white);
    border-radius: 22px;
    overflow: hidden;
    box-shadow: 0 10px 30px rgba(0,0,0,.18);
  }

  /* Front */
  .school-mark {
    position: absolute;
    top: 44px; left: 0; right: 0;
    display: flex;
    flex-direction: column;
    align-items: center;
    gap: 20px;
  }
  .school-mark .emblem {
    width: 150px; height: 150px;
    border-radius: 50%;
    background: radial-gradient(circle, #3a3a3a 0%, var(--mark-tone) 70%);
  }
  .school-mark .school-name {
    font-weight: 700;
    font-size: 30px;
    letter-spacing: 2px;
    text-transform: uppercase;
    color: var(--black);
    text-align: center;
    line-height: 1.1;
  }
  .contact {
    position: absolute;
    left: 22px; right: 22px; top: 330px;
    text-transform: uppercase;
    font-weight: 500;
  }
  .name-row {
    display: flex;
    align-items: flex-end;
    justify-content: space-between;
    border-bottom: 6px solid var(--red);
  }
  .name-row .person { font-size: 24px; font-weight: 700; line-height: 1.1; }
  .name-row .role {
    background: var(--red);
    color: var(--white);
    font-size: 13px;
    font-weight: 700;
    padding: 2px 8px 0;
  }
  .address {
    background: var(--grey);
    color: var(--white);
    font-size: 14px;
    line-height: 1.3;
    padding: 6px 10px;
    margin-top: 6px;
  }
  .bar {
    background: var(--black);
    color: var(--white);
    font-size: 15px;
    padding: 5px 10px;
    margin-top: 6px;
    display: flex;
    justify-content: space-between;
  }
  .bar .accent { color: var(--red); font-weight: 700; }
  .bar.centred { justify-content: center; }
  .link-row {
    display: flex;
    margin-top: 6px;
    font-size: 12.5px;
  }
  .link-row .label {
    background: var(--red);
    color: var(--white);
    font-weight: 700;
    width: 50px;
    padding: 5px 0;
    text-align: center;
  }
  .link-row .value {
    flex: 1;
    background: var(--black);
    color: var(--white);
    padding: 5px 8px;
    white-space: nowrap;
    overflow: hidden;
  }

  /* Back */
  .top-band { position: absolute; top: 0; left: 0; right: 0; height: 46px; background: var(--red); }
  .bottom-band {
    position: absolute; bottom: 0; left: 0; right: 0; height: 50px;
    background: var(--slate);
    color: var(--white);
    font-weight: 500;
    font-size: 18px;
    letter-spacing: 1px;
    display: flex; align-items: center; justify-content: center;
  }
  .quote {
    position: absolute;
    left: 34px; right: 34px;
    font-family: "Anton", "Impact", sans-serif;
    text-transform: uppercase;
    line-height: 1.08;
  }
  .quote .hl { color: var(--red); }
  .quote .source {
    display: block;
    font-family: "Oswald", sans-serif;
    font-weight: 700;
    font-size: 13px;
    margin-top: 8px;
  }
  .quote-education { top: 78px; font-size: 33px; }
  .quote-education .source { text-align: right; }
  .quote-be { top: 330px; font-size: 34px; }
  .quote-be .small { font-size: 17px; line-height: 1.2; display: block; }
</style>
</head>
<body>
  <article class="card card-front">
    <div class="school-mark">
      <div class="emblem" role="img" aria-label="School emblem area"></div>
      <div class="school-name">Garrow<br>Primary School</div>
    </div>
    <div class="contact">
      <div class="name-row"><span class="person">Miles Torvek</span><span class="role">Principal</span></div>
      <div class="address">318 Kessel Road Marrick Vale,<br>WA 6071.</div>
      <div class="bar"><span class="accent">T: (08) 9362 1504</span><span class="accent">F: (08) 9362 7190</span></div>
      <div class="bar centred"><span>M: 0413 582 947</span></div>
      <div class="link-row"><span class="label">Email</span><span class="value">Miles.Torvek@pupilhub.wa.edu.au</span></div>
      <div class="link-row"><span class="label">Web</span><span class="value">www.garrowps.wa.edu.au</span></div>
      <div class="link-row"><span class="label">Link</span><span class="value">au.linkfolio.net/in/milestorvek/</span></div>
    </div>
  </article>

  <article class="card card-back">
    <div class="top-band"></div>
    <blockquote class="quote quote-education">
      Education is the<br>
      <span class="hl">Most powerful weapon</span><br>
      which you can use to<br>
      <span class="hl">Change the world</span>
      <span class="source">Oswin Tembeka</span>
    </blockquote>
    <blockquote class="quote quote-be">
      Be who you are<br>
      And say what you feel
      <span class="small">Because those who mind don't matter<br>To those who matter don't mind</span>
      <span class="source">Dr Plimb</span>
    </blockquote>
    <div class="bottom-band">GARROWPS.WA.EDU.AU</div>
  </article>
</body>
</html>
```